Pages That Sell Services - book cover (front panel only)

I want a book cover (for print and ebook) in a distinctive, quirky style that can be repurposed for podcast artwork too. Full brief supplied.
The book is a practical, accessible handbook for anyone thinking about writing a book to build their business, with a wide range of tips and techniques to help plan, write, publishing and promote a book that’s integrated with your platform and works to build your reputation, network and credibility from day 1.
The target audience is experts in business, particularly owners of SMEs with an established online and offline platform (eg speaking, training, consulting) who want to add a book to take their business to the next level.
I want the design to be strong and distinctive, slightly quirky without being gimmicky, with the focus on typography.

Target Market(s)

Those writing a book based on their expertise to build their business

Industry/Entity Type

Publishing Company

Font styles to use
Serif
Sans Serif
Decorative

Colors

Designer to choose colors to be used in the design.

Requirements
Must have
• Commercially appealing book cover design, with application files and copyright supplied, front panel only, 5.5 x 8.5 inch format. Must work at both full size and thumbnail.
Nice to have
• A distinctive style that could be applied across other products in my portfolio.

```html
<!DOCTYPE html>
<html lang="en">
<head>
<meta charset="utf-8">
<title>Pages That Sell Services – Book Cover</title>
<link rel="stylesheet" href="https://fonts.googleapis.com/css2?family=Antonio:wght@300;400;600&display=swap">
<style>
  :root {
    --backdrop: #776e6b;
    --paper: #ffffff;
    --lime: #adc03a;
    --lime-soft: #c6d470;
    --teal: #0c5447;
    --mustard: #e6bb48;
    --edge: #2a2624;
  }
  * { margin: 0; padding: 0; box-sizing: border-box; }
  html, body {
    width: 1200px;
    height: 1200px;
    overflow: hidden;
    background: var(--backdrop);
  }
  .canvas {
    position: relative;
    width: 1200px;
    height: 1200px;
  }
  .cover {
    position: absolute;
    left: 418px;
    top: 321px;
    width: 341px;
    height: 525px;
    background: var(--paper);
    border: 1px solid var(--edge);
    overflow: hidden;
  }
  .tagline-band {
    position: absolute;
    left: 0; top: 0;
    width: 100%;
    height: 77px;
    background: var(--lime);
    display: flex;
    flex-direction: column;
    justify-content: center;
    align-items: center;
    font-family: "Antonio", "Arial Narrow", sans-serif;
    font-weight: 400;
    font-size: 20px;
    line-height: 24px;
    letter-spacing: 0.2px;
    color: var(--teal);
    text-transform: uppercase;
  }
  .desk-scene {
    position: absolute;
    left: 28px;
    top: 88px;
    width: 306px;
    height: 360px;
    border-radius: 40px 120px 60px 30px;
    background: radial-gradient(circle at 65% 40%, var(--lime-soft), var(--lime) 70%);
  }
  .book-face {
    position: absolute;
    left: 24px;
    top: 173px;
    width: 254px;
    height: 327px;
    background: var(--mustard);
  }
  .book-face svg {
    display: block;
    width: 254px;
    height: 327px;
  }
  .title {
    font-family: "Antonio", "Arial Narrow", sans-serif;
    fill: var(--teal);
  }
  .author {
    font-family: "Antonio", "Arial Narrow", sans-serif;
    font-weight: 300;
    fill: var(--paper);
  }
  .rule { stroke: var(--teal); stroke-width: 1.5; }
  .rule-dot { fill: var(--teal); }
</style>
</head>
<body>
  <main class="canvas">
    <article class="cover">
      <header class="tagline-band">
        <span>Clever ways to plan and write a book</span>
        <span>that works harder for your business</span>
      </header>

      <div class="desk-scene" role="img" aria-label="Illustration of a pen, percent sign, rising chart, clock, phone and coin spilling from behind an open book, in lime green"></div>

      <section class="book-face">
        <svg viewBox="0 0 254 327" xmlns="http://www.w3.org/2000/svg" aria-labelledby="cover-title">
          <title id="cover-title">Pages That Sell Services by Maren Holt</title>
          <text class="title" x="19" y="88" font-size="74" font-weight="300" textLength="218" lengthAdjust="spacingAndGlyphs">PAGES THAT SELL</text>
          <text class="title" x="19" y="215" font-size="142" font-weight="400" textLength="219" lengthAdjust="spacingAndGlyphs">SERVICES</text>
          <line class="rule" x1="33" y1="230" x2="217" y2="230"/>
          <circle class="rule-dot" cx="125" cy="230" r="2.5"/>
          <text class="author" x="35" y="310" font-size="79" textLength="181" lengthAdjust="spacingAndGlyphs">MAREN HOLT</text>
        </svg>
      </section>
    </article>
  </main>
</body>
</html>
```